Brochure Design Project

WE NEED A BROCHURE!!! - This should be easy and allows you to be creative! Corvane Nexus creates web and mobile portals for businesses in the health and wellness industry. The websites and mobile apps engage our clients' patients and consumers in health and wellness activities such as managing their conditions or losing weight. We leverage our large platform code-stack to build custom solutions for each client. We really love our website www.corvanenexus.com. So all we need is for someone to take that branding and create a 2-4 page brochure. The text is not that important as we can change it as needed. Mostly we just need the layout. We'd like to include the Zo Ka Lum colors and the JOURNAL font as included on our website.

• The 2 PDFs uploaded are 2 attempts that we aren't happy with but can be used as a reference only. Please be creative.

Must have the same branding language as our website www.corvanenexus.com - so that it looks like the same company.

Must have format/room for images. You can plug in stock photography if you'd like and we can buy or add in custom images later.

The font is JOURNAL for the zo/ka/lum. Other fonts are optional. Colors are:

Me – Green RGB 140, 188, 0
We – Blue RGB 11, 116, 187
Info – Orange RGB 237, 137, 33
Dark Gray – RGB 70, 80, 89
Med Gray – 114, 132, 154
Light Gray – 236, 238, 239

Thank you!

```html
<!DOCTYPE html>
<html lang="en">
<head>
<meta charset="utf-8">
<title>Corvane Nexus Brochure</title>
<link rel="stylesheet" href="https://fonts.googleapis.com/css2?family=Open+Sans:wght@600&family=Jost:wght@400&family=Caveat:wght@400&display=swap">
<style>
  :root {
    --green: #7ff205;
    --blue: #2680ff;
    --orange: #f07407;
    --dark-gray: #3d4b58;
    --med-gray: #6b90b0;
    --light-gray: #eff3f3;
    --white: #ffffff;
    --page-bg: #ffffff;
  }
  * { margin: 0; padding: 0; box-sizing: border-box; }
  html, body { width: 1200px; height: 1000px; overflow: hidden; background: var(--page-bg); }
  .canvas { position: relative; width: 1200px; height: 1000px; }
  .spread {
    position: absolute; left: 33px; top: 53px; width: 1135px; height: 877px;
    box-shadow: -6px 6px 10px rgba(0,0,0,0.55);
    background: var(--white);
  }
  .block { position: absolute; }
  .back-panel { left: 0; top: 0; width: 567px; height: 659px; background: var(--light-gray); }
  .back-stripe-orange { left: 0; top: 659px; width: 567px; height: 8px; background: var(--orange); }
  .back-stripe-green { left: 0; top: 667px; width: 567px; height: 15px; background: var(--green); }
  .back-band-blue { left: 0; top: 682px; width: 567px; height: 195px; background: var(--blue); }
  .spine { left: 567px; top: 0; width: 142px; height: 877px; background: var(--green); }
  .cover-blue { left: 709px; top: 0; width: 142px; height: 219px; background: var(--blue); }
  .photo-fruit {
    left: 851px; top: 0; width: 284px; height: 219px;
    background: radial-gradient(ellipse at 55% 50%, #f2a23a 0%, #e8c05a 35%, #c94a2a 60%, #fbfbf8 85%);
  }
  .photo-waist {
    left: 709px; top: 219px; width: 284px; height: 220px;
    background: linear-gradient(180deg, #f6f1ec 0%, #d7a585 30%, #5ec3e6 55%, #c98f6e 80%, #f6f1ec 100%);
  }
  .cover-orange { left: 993px; top: 219px; width: 142px; height: 220px; background: var(--orange); }
  .brand-name {
    position: absolute; font-family: "Open Sans", sans-serif; font-weight: 600;
    color: var(--dark-gray); font-size: 40px; letter-spacing: -0.5px; white-space: nowrap;
  }
  .back-brand { left: 0; width: 567px; top: 534px; text-align: center; }
  .back-contact {
    position: absolute; left: 0; width: 567px; top: 590px; text-align: center;
    font-family: "Jost", sans-serif; font-size: 15px; line-height: 22px; color: var(--dark-gray);
  }
  .app-phone { position: absolute; left: 742px; top: 487px; }
  .tagline { position: absolute; left: 842px; top: 505px; font-family: "Caveat", cursive; }
  .tagline-main { font-size: 46px; line-height: 50px; color: var(--dark-gray); }
  .tagline-main .zo { color: var(--green); }
  .tagline-main .ka { color: var(--blue); }
  .tagline-main .lum { color: var(--orange); }
  .tagline-sub { font-size: 25px; line-height: 28px; color: var(--dark-gray); margin-left: 6px; }
  .cover-stripe-gray { left: 709px; top: 659px; width: 426px; height: 23px; background: var(--med-gray); }
  .cover-stripe-orange { left: 709px; top: 682px; width: 426px; height: 8px; background: var(--orange); }
  .cover-stripe-green { left: 709px; top: 690px; width: 426px; height: 15px; background: var(--green); }
  .cover-stripe-blue { left: 709px; top: 705px; width: 426px; height: 10px; background: var(--blue); }
  .cover-stripe-dark { left: 709px; top: 715px; width: 426px; height: 12px; background: var(--dark-gray); }
  .cover-brand { left: 817px; top: 778px; }
</style>
</head>
<body>
<div class="canvas">
  <div class="spread">
    <!-- back cover -->
    <div class="block back-panel"></div>
    <div class="brand-name back-brand">corvane nexus</div>
    <div class="back-contact">www.corvanenexus.com<br>For a demo contact: info@corvanenexus.com</div>
    <div class="block back-stripe-orange"></div>
    <div class="block back-stripe-green"></div>
    <div class="block back-band-blue"></div>

    <!-- spine -->
    <div class="block spine"></div>

    <!-- front cover -->
    <div class="block cover-blue"></div>
    <div class="block photo-fruit" role="img" aria-label="Photo of stacked fruit slices with an orange, kiwi and pomegranate seeds"></div>
    <div class="block photo-waist" role="img" aria-label="Photo of a waist being measured with a tape measure"></div>
    <div class="block cover-orange"></div>

    <svg class="app-phone" width="80" height="126" viewBox="0 0 80 126" role="img" aria-label="Smartphone showing the mobile app">
      <rect x="2" y="2" width="72" height="120" rx="10" fill="#1f2327" transform="rotate(-6 38 62)"/>
      <rect x="10" y="20" width="56" height="82" rx="2" fill="#e9ecef" transform="rotate(-6 38 62)"/>
      <circle cx="43" cy="112" r="4" fill="#3a3f44"/>
    </svg>

    <div class="tagline">
      <div class="tagline-main"><span class="zo">zo</span> + <span class="ka">ka</span> + <span class="lum">lum</span></div>
      <div class="tagline-sub">learn more about our formula</div>
    </div>

    <div class="block cover-stripe-gray"></div>
    <div class="block cover-stripe-orange"></div>
    <div class="block cover-stripe-green"></div>
    <div class="block cover-stripe-blue"></div>
    <div class="block cover-stripe-dark"></div>
    <div class="brand-name cover-brand">corvane nexus</div>
  </div>
</div>
</body>
</html>
```